Stationery for Services Company
Business Cards, Letterhead and Compliment Slips
Hi FenwickStudio,
We really like Draft 15. There are a few small changes though:-
1. On the bus cards and letterhead the phone number ends with 667 and not 668 as previously advised. Could this please be amended.
2.On the letterhead at the bottom could we remove mobile phone number and instead include website address: www.norvelpartners.com, the main telephone number ending in 667 and a general e-mail address: info@norvelpartners.com.
Many Thanks,
C.

```html
<!DOCTYPE html>
<html lang="en">
<head>
<meta charset="utf-8">
<title>Norvel Partners Stationery</title>
<link href="https://fonts.googleapis.com/css2?family=Open+Sans:wght@400;600&display=swap" rel="stylesheet">
<style>
  :root {
    --blue: #34479a;
    --blue-soft: #5a6cae;
    --grey: #a9abae;
    --grey-light: #d6d7d9;
    --gold: #b8953a;
    --ink: #5c5e62;
    --paper: #ffffff;
    --edge: #dedfe1;
  }
  * { margin: 0; padding: 0; box-sizing: border-box; }
  html, body { width: 1200px; height: 1101px; overflow: hidden; background: var(--paper); }
  body { position: relative; font-family: "Open Sans", sans-serif; color: var(--ink); }

  .sheet { position: absolute; background: var(--paper); border: 1px solid var(--edge); box-shadow: 2px 3px 6px rgba(0,0,0,.12); overflow: hidden; }
  .sheet svg.band { position: absolute; left: 0; top: 0; }

  .brand { position: absolute; display: flex; align-items: center; gap: 10px; }
  .brand-dot { width: 16px; height: 16px; border-radius: 50%; background: var(--gold); flex: none; }
  .brand-name { font-weight: 600; color: var(--blue); white-space: nowrap; }

  /* Letterhead */
  .letterhead { left: 54px; top: 60px; width: 792px; height: 975px; }
  .letterhead .brand { left: 40px; top: 128px; }
  .letterhead .brand-name { font-size: 30px; }
  .letterhead-footer { position: absolute; left: 40px; bottom: 18px; font-size: 12px; line-height: 20px; white-space: nowrap; }
  .letterhead-footer .web { color: var(--blue); font-weight: 600; }

  /* Envelope */
  .envelope { left: 405px; top: 555px; width: 765px; height: 420px; z-index: 2; }
  .envelope .brand { left: 165px; top: 232px; }
  .envelope .brand-name { font-size: 26px; }
  .envelope-flap-name { position: absolute; left: 300px; top: 40px; font-size: 20px; font-weight: 600; color: rgba(255,255,255,.35); white-space: nowrap; }
  .envelope-address { position: absolute; left: 150px; top: 355px; font-size: 11px; white-space: nowrap; }

  /* Business card */
  .card { width: 321px; height: 198px; left: 849px; }
  .card-front { top: 60px; }
  .card-front .brand { left: 22px; top: 80px; }
  .card-front .brand-name { font-size: 19px; }
  .card-front .brand-dot { width: 11px; height: 11px; }
  .card-person { position: absolute; right: 14px; top: 34px; text-align: right; font-size: 9px; line-height: 12px; white-space: nowrap; }
  .card-person .name { color: var(--gold); font-weight: 600; font-size: 10px; }
  .card-contact { position: absolute; left: 0; right: 0; top: 132px; text-align: center; font-size: 7.5px; line-height: 11px; }

  .card-back { top: 285px; background: var(--blue); height: 195px; }
  .card-back .wordmark { position: absolute; left: 120px; top: 60px; font-size: 24px; font-weight: 600; color: var(--blue-soft); white-space: nowrap; }
  .card-back .web { position: absolute; left: 120px; top: 98px; font-size: 8px; color: var(--grey-light); letter-spacing: .5px; white-space: nowrap; }
</style>
</head>
<body>

<section class="sheet letterhead">
  <svg class="band" width="792" height="130" viewBox="0 0 792 130">
    <path d="M0 0 H792 V12 C560 40 260 55 0 100 Z" fill="var(--grey)"/>
    <path d="M0 108 C260 62 560 46 792 18" fill="none" stroke="var(--blue)" stroke-width="5"/>
  </svg>
  <div class="brand"><span class="brand-dot"></span><span class="brand-name">Norvel Partners</span></div>
  <footer class="letterhead-footer">
    <p>Office 410 4th Floor Harbour Point Tower Marina District</p>
    <p>P: +000 (4) 5550 667 &nbsp; info@norvelpartners.com &nbsp; <span class="web">www.norvelpartners.com</span></p>
  </footer>
</section>

<section class="sheet envelope">
  <svg class="band" width="765" height="220" viewBox="0 0 765 220">
    <path d="M0 120 C280 150 560 110 765 55 V95 C560 150 300 200 0 200 Z" fill="var(--grey)"/>
    <path d="M0 0 H765 V55 C560 110 280 150 0 120 Z" fill="var(--blue)"/>
    <path d="M0 124 C280 154 560 114 765 59" fill="none" stroke="var(--paper)" stroke-width="3"/>
  </svg>
  <p class="envelope-flap-name">Norvel Partners</p>
  <div class="brand"><span class="brand-dot"></span><span class="brand-name">Norvel Partners</span></div>
  <p class="envelope-address">Office 410 4th Floor Harbour Point Tower Marina District</p>
</section>

<section class="sheet card card-front">
  <svg class="band" width="321" height="70" viewBox="0 0 321 70">
    <path d="M0 0 H321 V20 C220 30 110 40 0 60 Z" fill="var(--grey)"/>
    <path d="M0 63 C110 43 220 33 321 23" fill="none" stroke="var(--blue)" stroke-width="3"/>
  </svg>
  <div class="card-person">
    <p class="name">Ada Mercer</p>
    <p>Consultant</p>
  </div>
  <div class="brand"><span class="brand-dot"></span><span class="brand-name">Norvel Partners</span></div>
  <div class="card-contact">
    <p>Office 410 4th Floor Harbour Point Tower</p>
    <p>Marina District</p>
    <p>T: +000 (4) 5550 667 &nbsp; F: +000 (4) 5550 668</p>
    <p>a.mercer@norvelpartners.com</p>
  </div>
</section>

<section class="sheet card card-back">
  <p class="wordmark">Norvel Partners</p>
  <p class="web">www.norvelpartners.com</p>
</section>

</body>
</html>
```